Evening of Discovery Annual Fundraising Dinner

I need a design for an invitation to our Evening of Discovery fundraising dinner.
The organization is called Halvern Joint Science Trust Foundation. (Find info at movewellfund.example)
Our organization tries to raise money to fund research into arthritis - all the different kinds of arthritis. We fund cutting edge research by giving grants to young scientists at different universities . I'm looking for an innovative design for the invitation to this event .
At this event we introduce our audience to to Scientists that we gave grants to in the previous year and tell them about the scientists who applied for grants this year. We also use the event to raise money towards these grants

Target Market(s)

Adults who suffer from Arthritis or who have relatives who suffer from arthritis and who want to learn more about the research being done to try to find a cure and who are willing to donate towards the cause

Industry/Entity Type

Foundation

Font styles to use
Sans Serif

Colors
ed2a32
0355a3

Requirements
Should not have
• We are NOT the Corlane Health Society we are a REsearch foundation .... Raising money for research .

```html
<!DOCTYPE html>
<html lang="en">
<head>
<meta charset="utf-8">
<title>Evening of Discovery – Fundraising Dinner Invitation</title>
<link rel="stylesheet" href="https://fonts.googleapis.com/css2?family=Open+Sans:wght@300;400;600;700;800&display=swap">
<style>
  :root {
    --ink: #050505;
    --red: #ed2a32;
    --blue: #1b7fd6;
    --brand-blue: #0355a3;
    --white: #ffffff;
    --page: #d9d9d7;
  }
  * { box-sizing: border-box; margin: 0; padding: 0; }
  html, body { width: 1108px; height: 1200px; overflow: hidden; background: var(--page); }
  body { font-family: "Open Sans", Arial, sans-serif; }

  .invitation {
    position: relative;
    width: 1108px; height: 1200px;
    background: var(--ink);
    color: var(--white);
    overflow: hidden;
  }

  .kicker {
    position: absolute; top: 52px; left: 0; width: 100%;
    text-align: center;
    font-size: 26px; font-weight: 400; letter-spacing: 16px;
  }
  .rule {
    position: absolute; top: 100px; left: 60px; width: 990px; height: 2px;
    background: var(--red);
  }
  .title {
    position: absolute; top: 108px; left: 0; width: 100%;
    text-align: center;
    font-size: 92px; font-weight: 300; line-height: 1.1;
    color: var(--blue); text-transform: uppercase; letter-spacing: -1px;
  }
  .subtitle {
    position: absolute; top: 226px; left: 0; width: 100%;
    text-align: center;
    font-size: 50px; font-weight: 800; line-height: 1;
    color: var(--red); letter-spacing: 10px; text-transform: uppercase;
  }

  .hero {
    position: absolute; top: 300px; left: 0; width: 1108px; height: 480px;
  }
  .hero-image {
    position: absolute; inset: 0;
    background:
      radial-gradient(ellipse 14% 16% at 72% 48%, rgba(237,70,60,.85), rgba(237,70,60,0) 100%),
      radial-gradient(ellipse 55% 24% at 50% 66%, rgba(235,235,235,.55), rgba(120,120,120,.15) 70%, rgba(0,0,0,0) 100%),
      var(--ink);
  }
  .hero-marks { position: absolute; inset: 0; overflow: visible; }

  .badge {
    position: absolute; top: 330px; left: 92px;
    width: 190px; height: 190px; border-radius: 50%;
    border: 2px solid var(--white);
    display: flex; align-items: center; justify-content: center;
    text-align: center;
    font-size: 21px; font-weight: 400; line-height: 1.15; text-transform: uppercase;
    transform: rotate(-8deg);
  }

  .details {
    position: absolute; top: 788px; left: 110px;
    font-size: 30px; line-height: 1.3;
  }
  .details p { margin-bottom: 6px; }
  .label { color: var(--red); font-weight: 700; text-transform: uppercase; }
  .value { color: var(--blue); font-weight: 400; }
  .venue { text-transform: uppercase; }
  .details .rsvp { color: var(--white); font-size: 24px; margin: 2px 0 0; }

  .brand {
    position: absolute; top: 900px; left: 800px; width: 260px;
    display: flex; flex-direction: column; align-items: center; gap: 14px;
  }
  .brand-dot { width: 100px; height: 100px; border-radius: 50%; background: var(--brand-blue); }
  .brand-name {
    font-size: 26px; font-weight: 700; line-height: 1.15;
    color: var(--blue); text-align: center; text-transform: uppercase;
  }

  .ticket-band {
    position: absolute; left: 0; bottom: 0; width: 100%; height: 92px;
    background: var(--red);
    display: flex; align-items: center; justify-content: center;
    font-size: 32px; font-weight: 400; color: var(--white);
  }
  .ticket-band strong { font-weight: 800; font-size: 38px; margin-left: 12px; }
</style>
</head>
<body>
<main class="invitation">
  <p class="kicker">+ INVITATION +</p>
  <div class="rule"></div>
  <h1 class="title">Evening of Discovery</h1>
  <h2 class="subtitle">Fundraising Dinner</h2>

  <section class="hero">
    <div class="hero-image" role="img" aria-label="X-ray photograph of an arthritic hand, with an inflamed joint glowing red"></div>
    <svg class="hero-marks" width="1108" height="480" viewBox="0 0 1108 480" aria-hidden="true">
      <g fill="none" stroke="#1b7fd6" stroke-width="3">
        <circle cx="400" cy="120" r="60"/>
        <circle cx="280" cy="250" r="36"/>
        <circle cx="905" cy="320" r="38"/>
        <circle cx="235" cy="436" r="36"/>
      </g>
      <circle cx="785" cy="230" r="78" fill="none" stroke="#ed2a32" stroke-width="3"/>
    </svg>
  </section>

  <div class="badge">Raising<br>funds for<br>arthritis<br>research</div>

  <section class="details">
    <p><span class="label">When:</span> <span class="value">Wednesday, April 5, 2017</span></p>
    <p><span class="label">Place:</span> <span class="value venue">Linden Hall Riverside</span><br>
       <span class="value">418 Harbor View Road, Terrace Level</span><br>
       <span class="value">Westbrook, CA 90000</span></p>
    <p><span class="label">Start time:</span> <span class="value">6:00pm to 11.30pm</span></p>
    <p><span class="label">Cost:</span> <span class="value">$120 per person</span></p>
    <p class="rsvp">Please RSVP by 7 March to info@movewellfund.example</p>
  </section>

  <div class="brand">
    <div class="brand-dot"></div>
    <p class="brand-name">Halvern Joint<br>Science Trust</p>
  </div>

  <footer class="ticket-band">Call to reserve your tickets on <strong>012 555 0147</strong></footer>
</main>
</body>
</html>
```